body balm label design

body balm tube design, current label design for other similar products
Need to have a design which can interchange between 3 different solutions
Quiet Orchard (Lavender + Vanilla)
Copper Trail (Eucalyptus + Mint)
Fern Hollow (Bergamot + Cedarwood)
Tube size:
2.5h x 3.25 w
Target Market(s)
natural, solution focused
Requirements
Must have
- relatable to existing brand designs, focus on features and benefits

```html
<!DOCTYPE html>
<html lang="en">
<head>
<meta charset="utf-8">
<title>Verdant Leaf – Calm~Balm Label Range</title>
<link rel="stylesheet" href="https://fonts.googleapis.com/css2?family=Raleway:wght@300;400;500&display=swap">
<style>
  :root {
    --canvas: #efedea;
    --label: #ffffff;
    --ink: #1f1f22;
    --ink-soft: #3a3a3e;
    --band: #7a2a80;
    --band-text: #ffffff;
    --lavender: #6b3f8f;
    --lavender-deep: #3d2a52;
    --vanilla: #e9e6da;
    --vanilla-leaf: #4e6a22;
    --eucalyptus: #6f8a7d;
    --eucalyptus-deep: #2f443a;
    --mint: #4f8a3a;
    --mint-deep: #1f4a1e;
    --bergamot: #8fb04a;
    --bergamot-deep: #3d5e1e;
    --cedar: #8b6a58;
    --cedar-deep: #4a3128;
  }
  * { box-sizing: border-box; margin: 0; padding: 0; }
  html, body { width: 1200px; height: 1200px; overflow: hidden; }
  body {
    background: var(--canvas);
    display: flex;
    align-items: center;
    justify-content: center;
    gap: 40px;
    font-family: "Raleway", sans-serif;
  }
  .label {
    position: relative;
    width: 340px;
    height: 770px;
    background: var(--label);
    overflow: hidden;
    box-shadow: 0 2px 10px rgba(0,0,0,0.08);
  }
  .brand {
    position: absolute;
    top: 84px;
    left: 0;
    width: 100%;
    text-align: center;
    color: var(--ink);
  }
  .brand-name {
    font-weight: 400;
    font-size: 22px;
    letter-spacing: 1px;
    line-height: 1;
  }
  .brand-tagline {
    font-weight: 400;
    font-size: 7px;
    letter-spacing: 2px;
    margin-top: 6px;
  }
  .product-name {
    position: absolute;
    top: 184px;
    width: 100%;
    text-align: center;
    font-weight: 300;
    font-size: 36px;
    line-height: 1;
    color: var(--ink);
  }
  .product-line {
    position: absolute;
    top: 234px;
    left: 30px;
    right: 30px;
    text-align: center;
    font-weight: 400;
    font-size: 16px;
    line-height: 1.2;
    color: var(--ink-soft);
    padding-bottom: 4px;
    border-bottom: 1px solid var(--ink-soft);
  }
  .product-details {
    position: absolute;
    top: 274px;
    width: 100%;
    text-align: center;
    font-size: 14px;
    line-height: 22px;
    color: var(--ink-soft);
  }
  .solution-band {
    position: absolute;
    top: 400px;
    left: 0;
    width: 100%;
    height: 56px;
    background: var(--band);
    color: var(--band-text);
    display: flex;
    align-items: center;
    justify-content: center;
    font-weight: 500;
    font-size: 22px;
    letter-spacing: 5px;
  }
  .ingredients {
    position: absolute;
    top: 456px;
    left: 0;
    width: 100%;
    height: 314px;
    display: flex;
  }
  .ingredient { flex: 1; }
  .lavender { background: linear-gradient(160deg, var(--lavender), var(--lavender-deep)); }
  .vanilla { background: radial-gradient(circle at 55% 40%, var(--vanilla) 0 22%, var(--vanilla-leaf) 70%); }
  .eucalyptus { background: linear-gradient(160deg, var(--eucalyptus), var(--eucalyptus-deep)); }
  .mint { background: linear-gradient(160deg, var(--mint), var(--mint-deep)); }
  .bergamot { background: radial-gradient(circle at 45% 60%, #c9dc8a 0 14%, var(--bergamot) 40%, var(--bergamot-deep)); }
  .cedar { background: linear-gradient(160deg, var(--cedar), var(--cedar-deep)); }
</style>
</head>
<body>
  <article class="label">
    <div class="brand">
      <div class="brand-name">VERDANT LEAF</div>
      <div class="brand-tagline">MADE FROM GARDEN OILS</div>
    </div>
    <h1 class="product-name">Calm~Balm</h1>
    <p class="product-line">Lorem Ipsum Dolor Consectetuer</p>
    <p class="product-details">Adipiscing Sed Elit<br>Diam Nonummy Euismod</p>
    <div class="solution-band">QUIET ORCHARD</div>
    <div class="ingredients">
      <div class="ingredient lavender" role="img" aria-label="Photo of lavender flowers"></div>
      <div class="ingredient vanilla" role="img" aria-label="Photo of white vanilla blossoms"></div>
    </div>
  </article>

  <article class="label">
    <div class="brand">
      <div class="brand-name">VERDANT LEAF</div>
      <div class="brand-tagline">MADE FROM GARDEN OILS</div>
    </div>
    <h1 class="product-name">Calm~Balm</h1>
    <p class="product-line">Lorem Ipsum Dolor Consectetuer</p>
    <p class="product-details">Adipiscing Sed Elit<br>Diam Nonummy Euismod</p>
    <div class="solution-band">COPPER TRAIL</div>
    <div class="ingredients">
      <div class="ingredient eucalyptus" role="img" aria-label="Photo of eucalyptus leaves"></div>
      <div class="ingredient mint" role="img" aria-label="Photo of fresh mint leaves"></div>
    </div>
  </article>

  <article class="label">
    <div class="brand">
      <div class="brand-name">VERDANT LEAF</div>
      <div class="brand-tagline">MADE FROM GARDEN OILS</div>
    </div>
    <h1 class="product-name">Calm~Balm</h1>
    <p class="product-line">Lorem Ipsum Dolor Consectetuer</p>
    <p class="product-details">Adipiscing Sed Elit<br>Diam Nonummy Euismod</p>
    <div class="solution-band">FERN HOLLOW</div>
    <div class="ingredients">
      <div class="ingredient bergamot" role="img" aria-label="Photo of bergamot fruits"></div>
      <div class="ingredient cedar" role="img" aria-label="Photo of a cedar cone with needles"></div>
    </div>
  </article>
</body>
</html>
```